Artificial intelligence, machine learning, and automation company needs a sexy business card design

We need a sleek and sexy business card design for an AI consulting company based in Philadelphia PA. We provide custom machine learning and automation solutions for companies of all shapes and sizes. The primary industries that we serve are pharmaceuticals, engineering, healthcare, and computer software. We would like the designs to be a black business card that uses green as a sleek accent color. The final design should communicate intelligence, cutting edge new-tech, and optimization.

Target Market(s)

C-level and VP level executives of multi-million annual companies. Mostly in Pharma, Healthcare, Real Estate, Retail, and Engineering

Industry/Entity Type

Computer Software

Contact Information for Business Card

Name: Jed Harlow
Title: CEO
Cell: 484 562 0937
Email: JedH@quillorbit.example
Website: www.QuillOrbit.example

Font styles to use
Sans Serif

Colors

Designer to choose colors to be used in the design.

Requirements
Must have
• 1) Attached Quillon Logo (either with colors or not/embossed)
• 2) "Artificial Intelligence" "Automation" and "Machine Learning"
• 3) "Quillon Laboratories" or "Quillon Labs" or "Quillon"
• 4) Sexy AF.
Nice to have
• Black card / dark card color, "Quillon Green" accent colors (in attached .ai file), Embossment of logo/name/etc, thick card stock, colored borders (on card sides, not front/back faces)
Should not have
• Should not be bland, or unsexy.

```html
<!DOCTYPE html>
<html lang="en">
<head>
<meta charset="utf-8">
<title>Quillon Laboratories – Business Card</title>
<link rel="stylesheet" href="https://fonts.googleapis.com/css2?family=Lato:wght@400;700;900&display=swap">
<style>
  :root {
    --backdrop: #3b3c3e;
    --quillon-green: #55c3b0;
    --card-dark: #4a4a4b;
    --ink-dark: #4d4d4f;
    --white: #ffffff;
  }
  * { box-sizing: border-box; margin: 0; padding: 0; }
  html, body {
    width: 1200px; height: 1000px; overflow: hidden;
    background: var(--backdrop);
    font-family: "Lato", Arial, sans-serif;
  }
  .canvas { position: relative; width: 1200px; height: 1000px; }

  .card {
    position: absolute;
    width: 600px; height: 340px;
    border-radius: 28px;
    overflow: hidden;
  }
  .card--front { left: 90px; top: 110px; background: var(--quillon-green); }
  .card--back  { left: 510px; top: 530px; background: var(--card-dark); }

  /* Front face */
  .front-brand {
    position: absolute; left: 62px; top: 112px;
    display: flex; align-items: center; gap: 24px;
  }
  .brand-square {
    width: 108px; height: 108px;
    border: 5px solid var(--ink-dark);
    flex: none;
  }
  .front-wordmark { color: var(--white); font-weight: 400; line-height: 1; }
  .front-wordmark .name { display: block; font-size: 64px; letter-spacing: 13px; }
  .front-wordmark .sub  { display: block; font-size: 26px; letter-spacing: 7.5px; margin-top: 10px; }

  /* Back face */
  .back-brand {
    position: absolute; left: 60px; top: 68px; width: 232px;
    display: flex; flex-direction: column; align-items: center;
  }
  .back-brand .brand-square {
    width: 150px; height: 150px;
    border-color: var(--quillon-green); border-width: 6px;
  }
  .back-wordmark { color: var(--white); font-weight: 400; text-align: center; line-height: 1; margin-top: 14px; }
  .back-wordmark .name { display: block; font-size: 30px; letter-spacing: 6px; }
  .back-wordmark .sub  { display: block; font-size: 13px; letter-spacing: 3.5px; margin-top: 5px; }

  .divider {
    position: absolute; left: 318px; top: 62px;
    width: 2px; height: 210px; background: var(--white);
  }

  .contact { position: absolute; left: 346px; top: 66px; color: var(--white); }
  .contact .person { font-size: 25px; font-weight: 900; color: var(--quillon-green); letter-spacing: 0.5px; line-height: 1.1; }
  .contact .role { font-size: 16px; font-weight: 700; margin-top: 2px; margin-bottom: 16px; }
  .contact-list { list-style: none; }
  .contact-list li {
    display: flex; align-items: center; gap: 14px;
    font-size: 17px; font-weight: 700; margin-bottom: 12px;
    white-space: nowrap;
  }
  .contact-icon {
    width: 24px; height: 24px; flex: none;
    border: 1.5px solid var(--quillon-green);
    display: flex; align-items: center; justify-content: center;
  }
  .contact-icon svg { width: 15px; height: 15px; }
  .accent { color: var(--quillon-green); }
</style>
</head>
<body>
<main class="canvas">

  <section class="card card--front" aria-label="Card front">
    <div class="front-brand">
      <div class="brand-square"></div>
      <div class="front-wordmark">
        <span class="name">QUILLON</span>
        <span class="sub">LABORATORIES</span>
      </div>
    </div>
  </section>

  <section class="card card--back" aria-label="Card back">
    <div class="back-brand">
      <div class="brand-square"></div>
      <div class="back-wordmark">
        <span class="name">QUILLON</span>
        <span class="sub">LABORATORIES</span>
      </div>
    </div>

    <div class="divider"></div>

    <div class="contact">
      <p class="person">JED HARLOW</p>
      <p class="role">CEO</p>
      <ul class="contact-list">
        <li>
          <span class="contact-icon">
            <svg viewBox="0 0 16 16" fill="#55c3b0"><path d="M4 1.5l2.2 3-1.3 1.6c.8 1.9 2.2 3.3 4.1 4.1l1.6-1.3 3 2.2-1.2 2.6C6.6 13.4 2.6 9.4 1.4 3.6z"/></svg>
          </span>
          484 562 0937
        </li>
        <li>
          <span class="contact-icon">
            <svg viewBox="0 0 16 16" fill="none" stroke="#55c3b0" stroke-width="1.6"><rect x="1.5" y="3.5" width="13" height="9"/><path d="M1.5 3.5L8 9l6.5-5.5"/></svg>
          </span>
          JedH@quillorbit.example
        </li>
        <li>
          <span class="contact-icon">
            <svg viewBox="0 0 16 16" fill="none" stroke="#55c3b0" stroke-width="1.3"><circle cx="8" cy="8" r="6.3"/><ellipse cx="8" cy="8" rx="2.8" ry="6.3"/><path d="M1.7 8h12.6"/></svg>
          </span>
          <span>www.<span class="accent">QuillOrbit</span>.example</span>
        </li>
      </ul>
    </div>
  </section>

</main>
</body>
</html>
```